Brochure Design Oakridge Capital Partners

Create a brochure, which sells my business. Utilise the website www.oakridgecapitalpartners.example for the details that need to go into the brochure. I would like 2 designs, one for a 4 page brochure and the other for a two page brochure (focus firstly on the 4 page).

The focus points are our 4 year rent guarantee and also out pitch that we are invested with them. Please see the website.

Need to focus on the main points as per the website, can use text from the website and the graphics where suitable.

On the 4 page brochure, first 3 pages to be info as per the website. On the 4 page of the brochure I would like the information included on the final 2 pages of the attached document (the investment property example). Please shrink this down, you do not need to include all the wording more so the figures.

The colours of the brochure to be blue, white and black

Target Market(s)

Property Investors

Industry/Entity Type

Business

Colors
0355a3
ffffff

Requirements
Must have
• Must have the main info on the website, (4 year rent guarantee) 'We are invested with you'
Nice to have
• Professional look

```html
<!DOCTYPE html>
<html lang="en">
<head>
<meta charset="utf-8">
<title>Oakridge Capital Partners – 4 Page Brochure</title>
<link href="https://fonts.googleapis.com/css2?family=Roboto:ital,wght@0,400;0,500;0,700;0,900;1,700&family=Playfair+Display:ital@1&display=swap" rel="stylesheet">
<style>
:root{
  --brand:#0355a3;
  --sky:#1b8fd4;
  --sky-soft:#5cb3e6;
  --navy:#0b2746;
  --night:#16345d;
  --ink:#141414;
  --grey:#6c6f74;
  --paper:#ffffff;
  --paper-shade:#f1f3f5;
  --table:#dfe3e8;
  --red:#e23b3b;
  --backdrop:#a8cfdb;
}
*{box-sizing:border-box;margin:0;padding:0}
html,body{width:1200px;height:1200px;overflow:hidden}
body{background:var(--backdrop);font-family:"Roboto",Arial,sans-serif;color:var(--ink);position:relative}
.spread{position:absolute;left:70px;width:1060px;height:375px;display:flex;box-shadow:0 6px 18px rgba(20,60,80,.25)}
.spread--cover{top:22px}
.spread--about{top:412px}
.spread--offer{top:802px}
.page{position:relative;width:530px;height:375px;overflow:hidden;background:var(--paper)}
.page--left{box-shadow:inset -10px 0 14px -10px rgba(0,0,0,.18)}
.page--right{box-shadow:inset 10px 0 14px -10px rgba(0,0,0,.18)}
.abs{position:absolute}

/* brand name lockup */
.brand{display:flex;align-items:center;gap:7px}
.brand__square{width:22px;height:22px;border:3px solid currentColor}
.brand__name{font-weight:700;letter-spacing:.3px;line-height:1}
.brand--light{color:#fff}
.brand--light .brand__square{border-color:var(--sky-soft)}

/* back cover */
.back__photo{left:0;top:0;width:530px;height:200px;background:linear-gradient(160deg,#1c3b5e 0%,#0c2643 55%,#0a1d33 100%)}
.back__blue{left:0;top:200px;width:530px;height:175px;background:linear-gradient(180deg,var(--sky) 0%,#1479bf 100%)}
.back__logo{left:60px;top:86px}
.back__logo .brand__name{font-size:22px}
.back__squares{right:0;top:0}
.contact{left:40px;top:292px;color:#fff;font-size:6.5px;line-height:1.45}
.contact__name{font-size:10px;font-weight:700;margin-bottom:3px}
.contact__web{font-weight:700;margin-top:3px}

/* front cover */
.front__photo{left:0;top:0;width:530px;height:375px;background:linear-gradient(180deg,#1d3a66 0%,#2b4770 35%,#3d5a58 58%,#3d6b34 75%,#2f5a26 100%)}
.front__logo{left:110px;top:40px}
.front__logo .brand__name{font-size:20px}
.front__headline{right:30px;top:252px;text-align:right;color:#fff}
.front__headline h1{font-size:24px;font-weight:900;letter-spacing:-.4px}
.front__headline p{font-size:7px;font-weight:700;letter-spacing:.8px;margin-top:4px}
.front__band{left:0;bottom:0;width:530px;height:20px;background:var(--sky)}
.front__band-line{left:0;bottom:20px;width:530px;height:3px;background:#fff}

/* common inner page parts */
.footer-bar{left:0;bottom:10px;width:530px;height:7px;background:var(--sky)}
.footer-line{left:0;bottom:20px;width:530px;height:1.5px;background:var(--sky)}
.footer-brand{color:var(--brand)}
.footer-brand .brand__square{width:11px;height:11px;border-width:2px}
.footer-brand .brand__name{font-size:9px}
.kicker{font-size:10px;font-weight:700;color:var(--ink)}
.heading{font-size:25px;font-weight:900;letter-spacing:-.6px;line-height:1;color:var(--ink)}
.heading em{font-style:normal;color:var(--sky)}
.body-copy{font-size:5.6px;line-height:1.5;color:#3c3f44}
.body-copy p+p{margin-top:3px}
.lead{color:var(--sky);font-weight:700}
.tagline{font-size:9px;font-weight:700;font-style:italic;color:var(--sky)}

/* about page */
.about__photo{left:0;top:0;width:530px;height:165px;background:linear-gradient(170deg,#eef0f2 0%,#d9dde1 45%,#b9bfc6 70%,#e8eaec 100%)}
.about__title{left:40px;top:182px}
.about__copy{left:40px;top:228px;width:450px}
.about__tagline{left:40px;top:320px}
.about__brand{left:40px;top:340px}

/* service page */
.service__map{left:0;top:0;width:530px;height:160px;background:linear-gradient(180deg,#dfe3e7 0%,#eef0f2 70%,#fff 100%)}
.service__title{left:34px;top:30px}
.service__title .heading{font-size:20px}
.service__intro{left:34px;top:80px;width:170px}
.wheel{left:290px;top:14px}
.steps{left:34px;top:160px;width:470px;display:grid;grid-template-columns:repeat(4,1fr);gap:10px 14px}
.step__art{height:44px;background:linear-gradient(135deg,#cfe4f3 0%,#9dc6e4 60%,#e9eef2 100%)}
.step__label{font-size:6px;font-weight:700;color:var(--sky);margin-top:3px}
.step__text{font-size:5px;line-height:1.4;color:#4a4d52;margin-top:1px}
.service__brand{right:40px;top:340px}

/* rent guarantee page */
.offer__kicker{left:150px;top:30px;font-size:12px;font-weight:700}
.offer__script{left:210px;top:28px;font-family:"Playfair Display",Georgia,serif;font-style:italic;font-size:40px;color:#d9dce0}
.offer__title{left:180px;top:48px;font-size:32px;font-weight:900;color:var(--sky);letter-spacing:-1px}
.offer__lock{left:170px;top:100px;width:150px;height:150px;border-radius:50%;background:radial-gradient(circle at 40% 38%,#a9d3f2 0%,#2a8ad0 40%,#0e4f8f 75%,rgba(14,79,143,0) 76%)}
.offer__guarantee{left:120px;top:262px;font-size:18px;font-weight:900;letter-spacing:-.4px}
.offer__copy{left:40px;top:290px;width:450px}
.offer__contact{left:40px;top:326px;font-size:6.5px;font-weight:700;color:var(--sky)}
.offer__brand{left:40px;top:343px}

/* example page */
.example__photo{right:0;top:0;width:200px;height:150px;background:linear-gradient(225deg,#e6e9ec 0%,#f4eee9 45%,rgba(255,255,255,0) 100%)}
.example__title{left:34px;top:24px}
.example__title .heading{font-size:16px}
.example__intro{left:34px;top:62px;width:260px}
.tables{left:34px;top:94px;width:460px;display:flex;gap:20px}
.tables__col{flex:1}
.table-head{background:var(--sky);color:#fff;font-size:6px;font-weight:700;padding:2px 4px;display:flex;justify-content:space-between;margin-top:4px}
.table-row{display:flex;justify-content:space-between;font-size:5.4px;padding:1.5px 4px;border-bottom:.5px solid var(--table)}
.table-row:nth-child(odd){background:var(--paper-shade)}
.table-row b{font-weight:700}
.table-row .neg{color:var(--red);font-weight:700}
.table-sub{font-size:8px;font-weight:700;margin-top:6px}
.growth__title{left:34px;top:232px;font-size:13px;font-weight:900;color:var(--ink);line-height:1}
.growth__title em{font-style:normal;color:var(--sky)}
.growth__copy{left:34px;top:264px;width:120px}
.chart{left:175px;top:226px}
.example__brand{left:34px;top:343px}
</style>
</head>
<body>

<!-- Outer spread: back cover + front cover -->
<section class="spread spread--cover" aria-label="Cover spread">
  <article class="page page--left back">
    <div class="abs back__photo" role="img" aria-label="Darkened night photograph of a suburban family home"></div>
    <div class="abs back__blue"></div>
    <svg class="abs back__squares" width="60" height="60" viewBox="0 0 60 60" aria-hidden="true">
      <rect x="38" y="10" width="12" height="12" fill="#1b8fd4"/>
      <rect x="28" y="26" width="7" height="7" fill="#1b8fd4"/>
    </svg>
    <div class="abs back__logo brand brand--light">
      <span class="brand__square"></span><span class="brand__name">Oakridge</span>
    </div>
    <address class="abs contact" style="font-style:normal">
      <div class="contact__name">Oakridge Capital Partners</div>
      Level 4, 12 Harbour Lane<br>
      Westbrook NSW 2000 Australia<br>
      Phone: 1300 555 010<br>
      Email: hello@oakridgecapitalpartners.example
      <div class="contact__web">www.oakridgecapitalpartners.example</div>
    </address>
  </article>

  <article class="page page--right front">
    <div class="abs front__photo" role="img" aria-label="Dusk photograph of a luxury home with pool, lawn and sun loungers"></div>
    <div class="abs front__logo brand brand--light">
      <span class="brand__square"></span><span class="brand__name">Oakridge Capital Partners</span>
    </div>
    <div class="abs front__headline">
      <h1>We Are Invested To You</h1>
      <p>LET'S BUILD YOUR PROPERTY PORTFOLIO TOGETHER</p>
    </div>
    <div class="abs front__band-line"></div>
    <div class="abs front__band"></div>
    <svg class="abs" style="left:24px;bottom:22px" width="24" height="24" viewBox="0 0 24 24" aria-hidden="true">
      <rect x="2" y="4" width="10" height="10" fill="#1b8fd4"/>
      <rect x="14" y="14" width="7" height="7" fill="#fff"/>
    </svg>
  </article>
</section>

<!-- Inner spread 1: About + service -->
<section class="spread spread--about" aria-label="About spread">
  <article class="page page--left about">
    <div class="abs about__photo" role="img" aria-label="Photograph of a bright office desk with a computer showing property charts"></div>
    <div class="abs about__title">
      <div class="kicker">Who We Are</div>
      <h2 class="heading">About <em>Oakridge</em></h2>
    </div>
    <div class="abs about__copy body-copy">
      <p><span class="lead">Oakridge Capital Partners</span> is a property investment firm helping everyday Australians build wealth through carefully selected residential property in growth areas across the country.</p>
      <p>Our team was formed by investors who wanted a better experience than the one they received. We research markets, source quality homes, negotiate on your behalf and stay with you long after settlement so your portfolio keeps working.</p>
      <p>Unlike sales agents, we only succeed when you do. That is why every property we recommend is backed by independent research, clear figures and a long term plan built around your goals and your budget.</p>
      <p>Whether you are buying your first investment or adding to an existing portfolio, we give you the knowledge and support to invest with confidence.</p>
    </div>
    <div class="abs about__tagline tagline">Knowledge is power, understand investing in property.</div>
    <div class="abs about__brand brand footer-brand">
      <span class="brand__square"></span><span class="brand__name">Oakridge</span>
    </div>
    <div class="abs footer-line"></div>
    <div class="abs footer-bar"></div>
  </article>

  <article class="page page--right service">
    <div class="abs service__map" role="img" aria-label="Faint grey world map background"></div>
    <div class="abs service__title">
      <div class="kicker" style="font-size:7px">We Are There</div>
      <h2 class="heading">Every <em>Step</em> Of<br>The Way</h2>
    </div>
    <div class="abs service__intro body-copy">
      <p>We don't just find you a great investment property, we are there every step of the journey to ensure a seamless stress free experience.</p>
    </div>
    <svg class="abs wheel" width="200" height="140" viewBox="0 0 200 140" aria-label="Seven step 360 degree service cycle">
      <g font-family="Roboto, Arial, sans-serif" text-anchor="middle">
        <circle cx="100" cy="70" r="26" fill="#111"/>
        <text x="100" y="67" fill="#5cb3e6" font-size="9" font-weight="700">360°</text>
        <text x="100" y="78" fill="#fff" font-size="8" font-weight="700">Service</text>
        <g fill="#5cb3e6">
          <circle cx="100" cy="18" r="15"/>
          <circle cx="143" cy="36" r="15"/>
          <circle cx="155" cy="82" r="15"/>
          <circle cx="126" cy="118" r="15"/>
          <circle cx="74" cy="118" r="15"/>
          <circle cx="45" cy="82" r="15"/>
          <circle cx="57" cy="36" r="15"/>
        </g>
        <g fill="#fff" font-size="8" font-weight="700">
          <text x="100" y="17">1</text><text x="143" y="35">2</text><text x="155" y="81">3</text>
          <text x="126" y="117">4</text><text x="74" y="117">5</text><text x="45" y="81">6</text><text x="57" y="35">7</text>
        </g>
        <g fill="#fff" font-size="3.6">
          <text x="100" y="23">Assess Capacity</text><text x="143" y="41">Set Goals</text><text x="155" y="87">Strategy</text>
          <text x="126" y="123">Hot Spots</text><text x="74" y="123">Find Property</text><text x="45" y="87">Purchase</text><text x="57" y="41">Manage</text>
        </g>
      </g>
    </svg>
    <div class="abs steps">
      <div class="step"><div class="step__art" role="img" aria-label="Illustration of financial documents"></div><div class="step__label">Assess Financial Capacity</div><div class="step__text">We review income, savings and borrowing power.</div></div>
      <div class="step"><div class="step__art" role="img" aria-label="Illustration of a property guide booklet"></div><div class="step__label">Establish Property Goals</div><div class="step__text">Together we define what success looks like.</div></div>
      <div class="step"><div class="step__art" role="img" aria-label="Illustration of a laptop with strategy charts"></div><div class="step__label">Evaluate Property Strategy</div><div class="step__text">A clear plan matched to your budget and timeline.</div></div>
      <div class="step"><div class="step__art" role="img" aria-label="Illustration of a market research report"></div><div class="step__label">Identify Market Hot Spots</div><div class="step__text">Research points us to areas with strong growth.</div></div>
      <div class="step"><div class="step__art" role="img" aria-label="Illustration of property listings"></div><div class="step__label">Find Suitable Property</div><div class="step__text">We shortlist homes that meet every criteria.</div></div>
      <div class="step"><div class="step__art" role="img" aria-label="Illustration of a contract being signed"></div><div class="step__label">Purchase</div><div class="step__text">We negotiate and guide you through settlement.</div></div>
      <div class="step"><div class="step__art" role="img" aria-label="Illustration of a tablet showing rental figures"></div><div class="step__label">Rent And Manage</div><div class="step__text">Tenants placed and the property cared for.</div></div>
    </div>
    <div class="abs service__brand brand footer-brand">
      <span class="brand__square"></span><span class="brand__name">Oakridge</span>
    </div>
    <div class="abs footer-line"></div>
    <div class="abs footer-bar"></div>
  </article>
</section>

<!-- Inner spread 2: Rent guarantee + investment example -->
<section class="spread spread--offer" aria-label="Rent guarantee and investment example spread">
  <article class="page page--left offer">
    <div class="abs offer__kicker">We are</div>
    <div class="abs offer__script">Invested</div>
    <div class="abs offer__title">With You.</div>
    <div class="abs offer__lock" role="img" aria-label="Illustration of a blue combination padlock"></div>
    <div class="abs offer__guarantee">4 Year Rent Guarantee</div>
    <div class="abs offer__copy body-copy">
      <p>We provide a 4 year rent guarantee on selected properties. From the day your property settles, your rental income is secured for four full years, so you know exactly what is coming in and can plan your investment with certainty. No vacancy worries, no gaps in income, just a steady return while your property grows in value.</p>
    </div>
    <div class="abs offer__contact">Contact Oakridge for further details on the terms and conditions of this offer.</div>
    <div class="abs offer__brand brand footer-brand">
      <span class="brand__square"></span><span class="brand__name">Oakridge</span>
    </div>
    <div class="abs footer-line"></div>
    <div class="abs footer-bar"></div>
  </article>

  <article class="page page--right example">
    <div class="abs example__photo" role="img" aria-label="Photograph of a hand writing figures with a pen"></div>
    <div class="abs example__title">
      <h2 class="heading"><em>Investment</em><br><em>Property</em> Example</h2>
    </div>
    <div class="abs example__intro body-copy">
      <p>The figures below show a typical purchase at $400,000 with rent guaranteed for four years. They are a guide only and your own figures will depend on your personal situation.</p>
    </div>
    <div class="abs tables">
      <div class="tables__col">
        <div class="table-head"><span>Initial Costs</span><span>$</span></div>
        <div class="table-row"><span>Stamp Duty</span><span>9,298 &nbsp;(land value $172,000)</span></div>
        <div class="table-row"><span>Solicitor</span><span>1,500</span></div>
        <div class="table-row"><b>TOTAL</b><b>10,798</b></div>
        <div class="table-sub">Ongoing Holding Profit/Loss</div>
        <div class="table-head"><span>Holding Costs</span><span>$</span></div>
        <div class="table-row"><span>Interest 4.5%</span><span>17,835</span></div>
        <div class="table-row"><span>Insurance</span><span>850</span></div>
        <div class="table-row"><span>Council Rates</span><span>1,400</span></div>
        <div class="table-row"><span>Management Fees</span><span>1,456</span></div>
        <div class="table-row"><b>TOTAL</b><span class="neg">21,541</span></div>
      </div>
      <div class="tables__col">
        <div class="table-head"><span>Profit/Loss</span><span>$</span></div>
        <div class="table-row"><span>Rent Guaranteed ($400 p/w)</span><span>20,800</span></div>
        <div class="table-row"><span>Less Holding Costs</span><span>(21,541)</span></div>
        <div class="table-row"><b>Gross Gain</b><span class="neg">-741</span></div>
        <div class="table-head"><span>Tax Deduction</span><span>$</span></div>
        <div class="table-row"><span>Gain</span><span>-741</span></div>
        <div class="table-row"><span>Depreciation (Plant &amp; Equip)</span><span>3,657</span></div>
        <div class="table-row"><span>Capital Works</span><span>4,800</span></div>
        <div class="table-row"><b>TOTAL DEDUCTIONS</b><b>9,198</b></div>
        <div class="table-row"><span>Tax Return (37%)</span><span>3,403</span></div>
        <div class="table-row"><b>PROFIT</b><b style="color:var(--sky)">2,662</b></div>
      </div>
    </div>
    <div class="abs growth__title"><em>Growth</em><br>Projection</div>
    <div class="abs growth__copy body-copy">
      <p>Using a modest growth rate of 6% per annum, the property value and your equity build steadily over five years while the rent guarantee covers most holding costs.</p>
    </div>
    <svg class="abs chart" width="320" height="115" viewBox="0 0 320 115" aria-label="Bar chart of property value and equity at 6 percent growth per annum over five years">
      <g font-family="Roboto, Arial, sans-serif">
        <text x="10" y="9" font-size="7" font-weight="700" fill="#141414"><tspan fill="#1b8fd4">6%</tspan> Growth per annum</text>
        <rect x="270" y="4" width="5" height="5" fill="#e23b3b"/><text x="278" y="9" font-size="5" fill="#555">Equity</text>
        <rect x="270" y="12" width="5" height="5" fill="#1b8fd4"/><text x="278" y="17" font-size="5" fill="#555">Value</text>
        <line x1="10" y1="80" x2="260" y2="80" stroke="#c9ced4" stroke-width=".7"/>
        <g fill="#1b8fd4">
          <rect x="30" y="62" width="22" height="18"/>
          <rect x="75" y="54" width="22" height="26"/>
          <rect x="120" y="45" width="22" height="35"/>
          <rect x="165" y="34" width="22" height="46"/>
          <rect x="210" y="22" width="22" height="58"/>
        </g>
        <g fill="#e23b3b">
          <rect x="30" y="70" width="22" height="10"/>
          <rect x="75" y="68" width="22" height="12"/>
          <rect x="120" y="66" width="22" height="14"/>
          <rect x="165" y="64" width="22" height="16"/>
          <rect x="210" y="62" width="22" height="18"/>
        </g>
        <rect x="10" y="84" width="250" height="8" fill="#1b8fd4"/>
        <g font-size="5" fill="#fff" font-weight="700" text-anchor="middle">
          <text x="41" y="90">Year 1</text><text x="86" y="90">Year 2</text><text x="131" y="90">Year 3</text><text x="176" y="90">Year 4</text><text x="221" y="90">Year 5</text>
        </g>
        <rect x="10" y="92" width="250" height="8" fill="#f1f3f5"/>
        <g font-size="5" fill="#333" text-anchor="middle">
          <text x="41" y="98">$424,000</text><text x="86" y="98">$449,440</text><text x="131" y="98">$476,406</text><text x="176" y="98">$504,991</text><text x="221" y="98">$535,290</text>
        </g>
        <g font-size="5" fill="#333" text-anchor="middle">
          <text x="41" y="107">$24,000</text><text x="86" y="107">$49,440</text><text x="131" y="107">$76,406</text><text x="176" y="107">$104,991</text><text x="221" y="107">$135,290</text>
        </g>
      </g>
    </svg>
    <div class="abs example__brand brand footer-brand">
      <span class="brand__square"></span><span class="brand__name">Oakridge</span>
    </div>
    <div class="abs footer-line"></div>
    <div class="abs footer-bar"></div>
  </article>
</section>

</body>
</html>
```